Dubai, Oman, Saudi, Qatar, Kuwait, Bahrain
IKO.CA a popular Canadian non profit is opening in the middle east and will require a website that appeals to the Arab world
Industry
Technology
Color Preferences
green and blue and similar to iko.ca
Our Ideas & Additional Information
iko.ca logo
use these websites as examples to copy and make similar websites
www.pvx.mg
www.iko.ca
www.zelrovanika.ba
IKO Arabic - Zawar Tech (Technology) non profit , foundation , association
Please try to use some arabic writing as well as latin alphabet for the name of the company
Zawar Tech (Technology)
Please see sample logos attached, dont worry about logo design we will add later
Target Market(s)
gcc
Number of Pages Required
1 page
Look and feel

```html
<!DOCTYPE html>
<html lang="en">
<head>
<meta charset="utf-8">
<title>Zawar Tech</title>
<link href="https://fonts.googleapis.com/css2?family=Cairo:wght@600&family=Lexend:wght@400;500&family=Roboto:wght@400;500;700&display=swap" rel="stylesheet">
<style>
:root{
  --navy:#0b2660;
  --green:#1b8a12;
  --green-dark:#136d0c;
  --blue:#1a73d0;
  --pale-blue:#e2ecf7;
  --pale-green:#e3f0d8;
  --text:#333;
  --muted:#666;
  --white:#fff;
}
*{margin:0;padding:0;box-sizing:border-box}
html,body{width:1200px;height:4468px;overflow:hidden}
body{position:relative;background:var(--white);font-family:"Roboto",sans-serif;color:var(--text)}
.abs{position:absolute}
.heading{font-family:"Lexend",sans-serif;font-weight:500;color:var(--navy)}
.rule{position:absolute;height:3px;width:56px;background:var(--green)}
.btn{position:absolute;display:flex;align-items:center;justify-content:center;border-radius:26px;font:700 13px "Roboto",sans-serif;color:var(--white);text-transform:uppercase}
.btn-green{background:var(--green)}
.btn-blue{background:var(--blue)}
.btn-outline{background:var(--white);color:var(--green)}
.ph{position:absolute;border-radius:50%}

/* nav */
.brand{left:140px;top:20px;display:flex;align-items:center;gap:10px;font:500 20px "Lexend",sans-serif;color:var(--green)}
.brand-dot{width:56px;height:56px;border-radius:50%;border:4px solid var(--green)}
.nav{left:337px;top:36px;display:flex;gap:31px;font:500 14px "Roboto",sans-serif;color:#222}
.nav .active{border-bottom:3px solid var(--blue);padding-bottom:3px}

/* hero */
.hero{left:30px;top:92px;width:1170px;height:576px;background:var(--navy);border-radius:288px 0 0 288px}
.hero-fade{left:700px;top:92px;width:500px;height:576px;background:linear-gradient(90deg,rgba(255,255,255,0),#eef3f6)}
.hero-name{left:182px;top:164px;width:270px;direction:rtl;text-align:right;font:600 62px/80px "Cairo",sans-serif;color:var(--white)}
.hero-name-sub{left:182px;top:236px;width:270px;direction:rtl;text-align:left;font:600 36px/60px "Cairo",sans-serif;color:var(--white)}
.hero-tag{left:182px;top:324px;width:370px;font:400 24px/33px "Lexend",sans-serif;color:var(--white)}
.dots{left:513px;top:612px;display:flex;gap:16px}
.dots span{width:9px;height:9px;border-radius:50%;background:#5b6f98}
.dots .on{background:var(--white)}

/* about */
.about-bg{left:0;top:694px;width:1200px;height:590px;background:linear-gradient(90deg,#dfe6ea 0%,#f4f7f8 40%,#fff 55%,#e3f1f2 100%)}
.about-text{left:619px;top:880px;width:435px;font:400 14px/29.5px "Roboto",sans-serif;color:var(--muted);text-align:justify}

/* green band */
.band{left:0;top:1283px;width:1200px;height:536px}
.band-title{left:144px;top:1358px;font:500 45px/56px "Lexend",sans-serif;color:var(--white)}
.band-text{left:144px;top:1512px;width:568px;font:400 14px/29.5px "Roboto",sans-serif;color:var(--white);text-align:justify}

/* services */
.card{position:absolute;width:416px;height:224px;border:1.5px solid #cfcfcf;background:var(--white)}
.card.r{border-radius:0 112px 112px 0}
.card.l{border-radius:112px 0 0 112px}
.card.hl{background:var(--pale-green)}
.card h3{position:absolute;top:48px;font:500 16px/23px "Roboto",sans-serif;color:#222;width:215px}
.card p{position:absolute;top:104px;width:255px;font:400 12.5px/20px "Roboto",sans-serif;color:#777}
.card .more{position:absolute;top:158px;font:700 13px "Roboto",sans-serif;color:var(--green)}
.card .ic{position:absolute;top:62px;width:100px;height:100px;border-radius:50%;display:flex;align-items:center;justify-content:center}
.card.r h3,.card.r p,.card.r .more{left:35px}
.card.r .ic{left:296px}
.card.l h3,.card.l p,.card.l .more{left:136px}
.card.l .ic{left:18px}

/* areas */
.areas{left:22px;top:2584px;width:1178px;height:537px;background:var(--pale-blue);border-radius:268px 0 0 268px}
.area{position:absolute;width:210px;height:210px;border-radius:50%;display:flex;align-items:center;justify-content:center;font:700 24px "Roboto",sans-serif;color:var(--white)}

/* reviews */
.quote{left:290px;top:3855px;width:620px;text-align:center;font:italic 400 16px/30px "Roboto",sans-serif;color:var(--white)}
.contact{top:4288px;display:flex;align-items:center;gap:16px;font:400 13px/21px "Roboto",sans-serif;color:var(--white)}
.cicon{width:40px;height:40px;border-radius:50%;border:1.5px solid var(--white);display:flex;align-items:center;justify-content:center;flex:none}
.social{top:4396px;width:30px;height:30px;border-radius:50%;border:1.5px solid var(--white)}
</style>
</head>
<body>

<!-- header -->
<div class="abs brand"><span class="brand-dot"></span>Zawar Tech</div>
<nav class="abs nav">
  <span class="active">Home</span><span>Donation</span><span>Youth activities</span><span>How we work</span><span>Blog</span><span>Contact Us</span>
</nav>
<div class="btn btn-green" style="left:919px;top:24px;width:135px;height:46px;font-size:12px">Book a pickup</div>

<!-- hero -->
<div class="abs hero-fade"></div>
<div class="abs hero"></div>
<div class="ph" style="left:570px;top:118px;width:594px;height:594px;background:var(--white)"></div>
<div class="ph" role="img" aria-label="Photo of two men in traditional Gulf dress working at a laptop" style="left:578px;top:126px;width:578px;height:578px;background:linear-gradient(160deg,#c9c2b8,#eef0f1 45%,#b9c2c8)"></div>
<div class="abs hero-name" lang="ar">زوار</div>
<div class="abs hero-name-sub" lang="ar">للتقنية</div>
<p class="abs hero-tag">Bridging technology and charity to empower communities across the Middle East.</p>
<div class="btn btn-green" style="left:182px;top:456px;width:184px;height:45px">Join our mission</div>
<div class="btn btn-blue" style="left:182px;top:512px;width:184px;height:46px">Donate now</div>
<div class="abs dots"><span></span><span class="on"></span><span></span></div>

<!-- about -->
<div class="abs about-bg" role="img" aria-label="Faded coastal city skyline"></div>
<svg class="abs" style="left:140px;top:764px" width="430" height="430" viewBox="0 0 430 430">
  <path d="M215 10 A205 205 0 1 1 50 340" fill="none" stroke="var(--green)" stroke-width="6"/>
  <circle cx="215" cy="215" r="190" fill="var(--white)"/>
</svg>
<div class="ph" role="img" aria-label="Laptop with network diagram overlay" style="left:172px;top:796px;width:366px;height:366px;background:radial-gradient(circle at 40% 40%,#5b6f8c,#2c3a52)"></div>
<div class="ph" role="img" aria-label="Smiling woman working at a laptop" style="left:346px;top:1030px;width:170px;height:170px;border:5px solid var(--white);background:linear-gradient(160deg,#e8e0d4,#9a7c63)"></div>
<div class="abs heading" style="left:619px;top:790px;font-size:44px">About Us</div>
<div class="rule" style="left:619px;top:849px"></div>
<p class="abs about-text">Sed ut perspiciatis unde omnis iste natus error sit voluptatem accusantium doloremque laudantium, totam rem aperiam, eaque ipsa quae ab illo inventore veritatis et quasi architecto beatae vitae dicta sunt explicabo. Nemo enim ipsam voluptatem quia voluptas sit aspernatur aut odit aut fugit, sed quia consequuntur magni dolores eos qui ratione voluptatem sequi nesciunt. Neque porro quisquam est, qui dolorem ipsum quia dolor sit amet, consectetur</p>
<div class="btn btn-blue" style="left:619px;top:1113px;width:144px;height:45px">Read more</div>

<!-- opportunities band -->
<svg class="abs band" width="1200" height="536" viewBox="0 0 1200 536">
  <path d="M0 0 H800 A300 250 0 0 1 760 536 H0 Z" fill="var(--green)"/>
  <path d="M970 45 A220 220 0 0 1 960 500" fill="none" stroke="var(--green)" stroke-width="6"/>
</svg>
<div class="ph" style="left:768px;top:1356px;width:380px;height:380px;background:var(--white)"></div>
<div class="ph" role="img" aria-label="Smiling woman using a laptop" style="left:776px;top:1364px;width:364px;height:364px;background:linear-gradient(150deg,#f2f2f2,#d8d3cf 50%,#6e5646)"></div>
<div class="ph" style="left:754px;top:1262px;width:226px;height:226px;background:var(--white)"></div>
<div class="ph" role="img" aria-label="Donation box filled with old keyboards" style="left:762px;top:1270px;width:210px;height:210px;background:linear-gradient(180deg,#2e2e2e,#8f9498 60%,#c9cbcc)"></div>
<h2 class="abs band-title">Give New Opportunities<br>In The Most Secure Way</h2>
<div class="rule" style="left:144px;top:1476px;background:var(--white)"></div>
<p class="abs band-text">Sed ut perspiciatis unde omnis iste natus error sit voluptatem accusantium doloremque laudantium, totam rem aperiam, eaque ipsa quae ab illo inventore veritatis et quasi architecto beatae vitae dicta sunt explicabo. Nemo enim ipsam voluptatem quia voluptas sit aspernatur aut odit aut fugit, sed quia consequuntur magni dolores eos qui ratione voluptatem seque porro quisquam est, qui dolorem ipsum</p>
<div class="btn btn-outline" style="left:144px;top:1685px;width:144px;height:49px">Read more</div>

<!-- what we do -->
<div class="abs heading" style="left:0;width:1200px;text-align:center;top:1906px;font-size:43px">What We Do</div>
<div class="rule" style="left:572px;top:1976px"></div>

<div class="card r" style="left:165px;top:2020px">
  <h3>Your Electronics Live On Helping Those In Need</h3>
  <p>Sed ut perspiciatis unde omnis iste natus error sit voluptatem accusantium</p>
  <span class="more">READ MORE</span>
  <span class="ic" style="background:var(--green)"><svg width="44" height="34" viewBox="0 0 44 34"><rect x="6" y="2" width="32" height="22" rx="2" fill="none" stroke="#fff" stroke-width="4"/><rect x="0" y="27" width="44" height="5" rx="2" fill="#fff"/></svg></span>
</div>
<div class="card l" style="left:619px;top:2020px">
  <h3>Your Information Is Removed Safely &amp; Securely</h3>
  <p>Sed ut perspiciatis unde omnis iste natus error sit voluptatem accusantium</p>
  <span class="more">READ MORE</span>
  <span class="ic" style="background:var(--navy)"><svg width="32" height="40" viewBox="0 0 32 40"><path d="M7 17 V11 A9 9 0 0 1 25 11 V17" fill="none" stroke="#fff" stroke-width="4"/><rect x="2" y="17" width="28" height="22" rx="3" fill="#fff"/></svg></span>
</div>
<div class="card r" style="left:165px;top:2266px">
  <h3>We Offer On-Site Destruction Of Your Information</h3>
  <p>Sed ut perspiciatis unde omnis iste natus error sit voluptatem accusantium</p>
  <span class="more">READ MORE</span>
  <span class="ic" style="background:var(--navy)"><svg width="30" height="40" viewBox="0 0 30 40"><rect x="2" y="0" width="26" height="40" fill="#fff"/><g fill="var(--navy)"><rect x="7" y="5" width="5" height="5"/><rect x="18" y="5" width="5" height="5"/><rect x="7" y="15" width="5" height="5"/><rect x="18" y="15" width="5" height="5"/><rect x="11" y="28" width="8" height="12"/></g></svg></span>
</div>
<div class="card l hl" style="left:619px;top:2266px">
  <h3>We Can Pick Up Electronics From Your Location</h3>
  <p>Sed ut perspiciatis unde omnis iste natus error sit voluptatem accusantium</p>
  <span class="more">READ MORE</span>
  <span class="ic" style="background:var(--green)"><svg width="46" height="34" viewBox="0 0 46 34"><rect x="0" y="2" width="28" height="22" rx="2" fill="#fff"/><path d="M30 9 H39 L46 17 V26 H30 Z" fill="#fff"/><circle cx="10" cy="28" r="5" fill="#fff" stroke="var(--green)" stroke-width="2"/><circle cx="37" cy="28" r="5" fill="#fff" stroke="var(--green)" stroke-width="2"/></svg></span>
</div>
<div class="abs" role="img" aria-label="Woman holding a laptop" style="left:968px;top:2355px;width:232px;height:232px;border-radius:40% 40% 0 0;background:linear-gradient(180deg,#3b2a22,#4a6b91 60%,#d7dde6)"></div>

<!-- target areas -->
<div class="abs areas"></div>
<div class="abs heading" style="left:0;width:1200px;text-align:center;top:2690px;font-size:43px">Our Target Areas Are</div>
<div class="rule" style="left:572px;top:2755px"></div>
<svg class="abs" style="left:80px;top:2876px" width="36" height="64" viewBox="0 0 36 64"><path d="M34 2 L3 32 L34 62" fill="none" stroke="#9fb3cc" stroke-width="2"/></svg>
<svg class="abs" style="left:1086px;top:2876px" width="36" height="64" viewBox="0 0 36 64"><path d="M2 2 L33 32 L2 62" fill="none" stroke="#9fb3cc" stroke-width="2"/></svg>
<div class="area" role="img" aria-label="Dubai skyline at dusk" style="left:146px;top:2803px;background:linear-gradient(180deg,#4d6d9d,#1f2c4a 55%,#c08a3e)">DUBAI</div>
<div class="area" role="img" aria-label="Grand mosque in Oman" style="left:379px;top:2803px;border:3px solid var(--green);background:linear-gradient(180deg,#8fb4d4,#c6b89a 60%,#3f5a88)">OMAN</div>
<div class="area" role="img" aria-label="Riyadh skyline at night" style="left:611px;top:2803px;background:linear-gradient(180deg,#101c3d,#28407a 55%,#1a1f36)">SAUDI</div>
<div class="area" role="img" aria-label="Doha towers at night" style="left:844px;top:2803px;background:linear-gradient(180deg,#233352,#6b4d45 60%,#141a2c)">QATAR</div>

<!-- certifications -->
<div class="abs heading" style="left:0;width:1200px;text-align:center;top:3236px;font-size:44px;line-height:58px">ISO-Certified Excellence in Security,<br>Quality &amp; Sustainability</div>
<div class="rule" style="left:572px;top:3375px"></div>
<svg class="abs" style="left:317px;top:3429px" width="566" height="164" viewBox="0 0 566 164">
  <g fill="none" stroke="#666" stroke-width="3">
    <circle cx="82" cy="82" r="78"/><circle cx="82" cy="82" r="56"/>
    <circle cx="281" cy="82" r="78"/><circle cx="281" cy="82" r="50" fill="#555"/>
    <circle cx="481" cy="82" r="78"/><circle cx="481" cy="82" r="56"/>
  </g>
</svg>

<!-- reviews + footer -->
<svg class="abs" style="left:0;top:3960px" width="1200" height="508" viewBox="0 0 1200 508">
  <path d="M0 150 C300 80 900 80 1200 150 V508 H0 Z" fill="var(--navy)"/>
</svg>
<div class="abs" role="img" aria-label="Man in traditional dress behind green tint" style="left:144px;top:3676px;width:912px;height:390px;border-radius:195px;background:linear-gradient(90deg,#1b8a12,#2a9a20 60%,#1f7d16)"></div>
<div class="abs heading" style="left:0;width:1200px;text-align:center;top:3722px;font-size:44px;color:var(--white)">Customer Reviews</div>
<div class="rule" style="left:572px;top:3788px;background:var(--white)"></div>
<svg class="abs" style="left:190px;top:3844px" width="36" height="64" viewBox="0 0 36 64"><path d="M34 2 L3 32 L34 62" fill="none" stroke="#bfe0b9" stroke-width="2"/></svg>
<svg class="abs" style="left:964px;top:3844px" width="36" height="64" viewBox="0 0 36 64"><path d="M2 2 L33 32 L2 62" fill="none" stroke="#bfe0b9" stroke-width="2"/></svg>
<p class="abs quote">“Sed ut perspiciatis unde omnis iste natus error sit voluptatem accusantium doloremque laudantium, totam rem aperiam, eaque ipsa quae ab illo inventore veritatis et quasi architecto beatae vitae dicta sunt explicabo”</p>
<div class="abs" style="left:0;width:1200px;text-align:center;top:3971px;font:italic 500 17px Roboto,sans-serif;color:var(--white)">-John Doe <span style="font-style:normal;letter-spacing:1px">★★★★★</span></div>

<div class="abs" style="left:165px;top:4140px;font:500 42px Lexend,sans-serif;color:var(--white)">Want to donate?</div>
<div class="rule" style="left:165px;top:4196px;background:var(--white)"></div>
<div class="btn btn-blue" style="left:661px;top:4151px;width:184px;height:46px">Donate now</div>
<div class="btn btn-green" style="left:851px;top:4151px;width:184px;height:46px">Contact us</div>
<div class="abs" style="left:0;top:4257px;width:1200px;height:1px;background:#2b437a"></div>

<div class="abs contact" style="left:248px">
  <span class="cicon"><svg width="14" height="18" viewBox="0 0 14 18"><path d="M7 1 A6 6 0 0 1 13 7 C13 11 7 17 7 17 C7 17 1 11 1 7 A6 6 0 0 1 7 1Z" fill="none" stroke="#fff" stroke-width="1.6"/><circle cx="7" cy="7" r="2" fill="#fff"/></svg></span>
  <span>314,At vero eos et accu<br>samus et iusto odio dimos ducimu</span>
</div>
<div class="abs contact" style="left:556px">
  <span class="cicon" style="background:var(--green);border-color:var(--green)"><svg width="16" height="16" viewBox="0 0 16 16"><path d="M3 1 L6 1 L7 5 L5 6.5 C6 9 7 10 9.5 11 L11 9 L15 10 V13 C15 14 14 15 13 15 C6 14 2 10 1 3 C1 2 2 1 3 1Z" fill="#fff"/></svg></span>
  <span>1 888 888 8888</span>
</div>
<div class="abs contact" style="left:740px">
  <span class="cicon"><svg width="16" height="12" viewBox="0 0 16 12"><rect x="0" y="0" width="16" height="12" rx="1.5" fill="#fff"/><path d="M0.5 1 L8 7 L15.5 1" fill="none" stroke="var(--navy)" stroke-width="1.5"/></svg></span>
  <span>info@companyname.com</span>
</div>

<div class="abs" style="left:144px;top:4405px;font:400 12px Roboto,sans-serif;color:var(--white)">Copyrights © 2025, Companyname.All rights reserved &nbsp;|&nbsp; Privacy Policy &nbsp;|&nbsp; Terms of use</div>
<span class="abs social" style="left:949px"></span>
<span class="abs social" style="left:987px;background:var(--white)"></span>
<span class="abs social" style="left:1025px"></span>

</body>
</html>
```